Upscale business cards needed for family office

We would like professional business cards created for employees of our family office. Relatively simple and straightforward, but also with a unique element to set them apart. Probably stick with neutral and simple colors that mesh well with the colors in the logo. We need space for the traditional elements, including name, title, address, email/phone number.

Industry/Entity Type

Business

Contact Information for Business Card

Space for name, title, phone number, email, address

```html
<!DOCTYPE html>
<html lang="en">
<head>
<meta charset="utf-8">
<title>M&amp;L Business Card – John Doe</title>
<link rel="stylesheet" href="https://fonts.googleapis.com/css2?family=Open+Sans:wght@400;600;700&display=swap">
<style>
  :root {
    --card-mint: #d9fbf0;
    --card-charcoal: #2a3233;
    --stripe-white: #ffffff;
    --stripe-cyan: #3bbfe0;
    --stripe-blue: #3b74f0;
    --ink: #1a0f12;
    --ink-soft: #111111;
    --brand-tile: #9fb3b5;
  }
  * { margin: 0; padding: 0; box-sizing: border-box; }
  html, body {
    width: 700px;
    height: 1200px;
    overflow: hidden;
    background: var(--card-mint);
  }
  .card {
    position: relative;
    width: 700px;
    height: 1200px;
    background: var(--card-mint);
    font-family: "Open Sans", sans-serif;
    color: var(--ink-soft);
    overflow: hidden;
  }
  .card-backdrop {
    position: absolute;
    inset: 0;
    width: 700px;
    height: 1200px;
  }
  .brand {
    position: absolute;
    left: 96px;
    top: 170px;
    display: flex;
    align-items: center;
    gap: 18px;
  }
  .brand-square {
    width: 52px;
    height: 52px;
    background: var(--brand-tile);
  }
  .brand-name {
    font-size: 64px;
    font-weight: 400;
    line-height: 1;
    color: var(--card-mint);
  }
  .person {
    position: absolute;
    left: 0;
    width: 700px;
    text-align: center;
  }
  .person-name {
    top: 574px;
    font-size: 68px;
    font-weight: 700;
    line-height: 80px;
    letter-spacing: -0.5px;
    color: var(--ink);
  }
  .person-title {
    top: 650px;
    font-size: 44px;
    font-weight: 400;
    line-height: 52px;
  }
  .contact-list {
    position: absolute;
    left: 0;
    top: 770px;
    width: 700px;
    list-style: none;
    text-align: center;
    font-size: 34px;
    line-height: 74px;
  }
</style>
</head>
<body>
  <main class="card">
    <svg class="card-backdrop" viewBox="0 0 700 1200" xmlns="http://www.w3.org/2000/svg">
      <polygon points="0,0 667,0 0,667" fill="var(--card-charcoal)" role="img" aria-label="Dark textured linen panel"/>
      <polygon points="667,0 687,0 0,687 0,667" fill="var(--stripe-white)"/>
      <polygon points="687,0 717,0 0,717 0,687" fill="var(--stripe-cyan)"/>
      <polygon points="717,0 733,0 0,733 0,717" fill="var(--stripe-white)"/>
      <polygon points="733,0 772,0 0,772 0,733" fill="var(--stripe-blue)"/>
    </svg>

    <div class="brand">
      <span class="brand-square"></span>
      <span class="brand-name">M&amp;L</span>
    </div>

    <h1 class="person person-name">John Doe</h1>
    <p class="person person-title">managing director</p>

    <ul class="contact-list">
      <li class="contact-office">office 428.555.0164</li>
      <li class="contact-cell">cell 209.555.0137</li>
      <li class="contact-email">johndoe@example.com</li>
      <li class="contact-street">4821, NE 14th St</li>
      <li class="contact-city">Brindle, WA 98012</li>
    </ul>
  </main>
</body>
</html>
```